Tillbrook Direct Website

We are looking to update our consumer direct site. Needs to be powersports focused (motorcycle, ATV, boats, and personal watercrafts), but we are an insurance company so we need it to be classy...
We currently have three other "shield" logos on there that we will replace with basically the same shield but in green. We need an icon to:
1. Report a claim
2. Make a payment
3. Retrieve a quote
4. Print ID Card
5. Other Products
Work your magic! Thanks!
Updates
Project Deadline Extended
Reason: One of the decision makers will be out of the office until next week so we will provide our response next Tuesday. Thank you for your patience!
Industry/Entity Type
Insurance
Look and feel
Each slider illustrates characteristics of the customer's brand and the style your logo design should communicate.

```html
<!DOCTYPE html>
<html lang="en">
<head>
<meta charset="utf-8">
<title>Tillbrook Powersports Insurance</title>
<link rel="stylesheet" href="https://fonts.googleapis.com/css2?family=Arimo:wght@400;700&family=PT+Sans:wght@400;700&family=Fjalla+One&display=swap">
<style>
:root{
  --ink:#222;
  --grey-text:#555;
  --label:#444;
  --green:#0b6b35;
  --green-dark:#06451f;
  --orange:#c2740f;
  --orange-light:#e09a2a;
  --leaf:#6a9b3b;
  --sky:#6b8fbe;
  --panel:#f4f4f4;
  --field:#bbb7b4;
  --line:#c9c9c9;
}
*{box-sizing:border-box;margin:0;padding:0}
html,body{width:932px;height:1200px;overflow:hidden;background:#fff}
body{position:relative;font-family:"PT Sans",sans-serif;color:var(--ink)}
a{color:inherit;text-decoration:none}

.utility{position:absolute;top:18px;right:22px;font-size:12.5px;font-weight:700;color:#111;display:flex;gap:0}
.utility a{padding:0 0 0 0}
.utility .sep{margin:0 18px}
.utility .sep.short{margin:0 8px}

.brand{position:absolute;left:30px;top:34px;display:flex;align-items:center;gap:10px;z-index:3}
.brand-mark{width:26px;height:26px;background:var(--green);border-radius:50%}
.brand-name{font-family:"PT Sans",sans-serif;font-weight:700;font-size:24px;color:var(--green);line-height:1}

.main-nav{position:absolute;top:88px;left:0;width:932px;height:69px;background:linear-gradient(#fdfdfd,#e2e2e2);border-top:1px solid #d2d2d2;border-bottom:1px solid #c8c8c8}
.main-nav ul{list-style:none;position:absolute;left:0;top:0;height:100%;width:100%}
.main-nav li{position:absolute;top:0;height:100%;display:flex;align-items:center;font-size:15px;color:#333}
.main-nav li.active{background:linear-gradient(var(--green),var(--green-dark));color:#fff;border-top:3px solid #033;top:1px;height:66px;justify-content:center}
.main-nav .bar{font-size:13px;color:#333}

.showcase{position:absolute;top:157px;left:0;width:932px;display:flex}
.product{position:relative;height:529px;background:var(--panel)}
.product + .product{border-left:1px solid #fff}
.product-photo{height:223px}
.photo-moto{background:linear-gradient(90deg,#111 0%,#3a2a2a 40%,#b01a1f 55%,#222 100%)}
.photo-boat{background:linear-gradient(180deg,#203c66 0%,#345a8c 45%,#e8eef4 60%,#1f3e6e 100%)}
.photo-water{background:linear-gradient(180deg,#6eb9b0 0%,#2c7f86 50%,#d7ecec 75%,#3e8a91 100%)}
.product-tab{height:52px;display:flex;align-items:center;padding-left:28px;gap:12px;font-family:"Fjalla One",sans-serif;color:#fff;font-size:15px;letter-spacing:.3px;text-transform:uppercase}
.tab-moto{background:linear-gradient(var(--orange-light),var(--orange))}
.tab-boat{background:linear-gradient(#7fae4c,var(--leaf))}
.tab-water{background:linear-gradient(#82a3cd,var(--sky))}
.tab-dot{width:13px;height:13px;border-radius:50%;background:radial-gradient(circle at 40% 35%,#fff 0 25%,#f3d79b 45%,#a86a10 100%)}
.tab-boat .tab-dot{background:radial-gradient(circle at 40% 35%,#fff 0 25%,#cfe3b3 45%,#4b7b22 100%)}
.tab-water .tab-dot{background:radial-gradient(circle at 40% 35%,#fff 0 25%,#cfe0f4 45%,#3a6aa5 100%)}
.product-body{padding:36px 30px 0 29px;font-family:"Arimo",sans-serif;background:linear-gradient(90deg,#ececec,#f7f7f7 12%,#f7f7f7 88%,#ececec);height:254px;position:relative}
.lead{font-size:15.5px;line-height:21px;margin-bottom:13px}
.lead.moto{color:var(--orange)}
.lead.boat{color:var(--leaf)}
.lead.water{color:#3a7fd0}
.copy{font-size:12.3px;line-height:17.5px;color:var(--grey-text)}
.read-more{position:absolute;left:30px;bottom:20px;width:87px;height:19px;border:1px solid #aaa;border-radius:10px;background:linear-gradient(#fff,#e6e6e6);font-size:11.5px;color:#c0392b;display:flex;align-items:center;justify-content:center}

.services{position:absolute;top:686px;left:0;width:620px;height:332px}
.service{position:absolute;display:flex;align-items:center;gap:15px;font-family:"Fjalla One",sans-serif;font-size:22.5px;color:var(--label);letter-spacing:.3px}
.service svg{width:47px;height:47px;display:block}
.divider{position:absolute;left:37px;width:496px;border-top:1px dotted #777}

.quote{position:absolute;left:621px;top:692px;width:302px;height:315px;border:1px solid #ccc;background:#f6f6f6}
.quote-head{height:45px;margin:-1px -1px 0;border-top:4px solid var(--orange-light);background:linear-gradient(#d07f16,var(--orange));display:flex;align-items:center;padding-left:26px;gap:12px;font-family:"Fjalla One",sans-serif;color:#fff;font-size:15px;text-transform:uppercase}
.quote label{position:absolute;left:18px;font-size:13px;font-weight:700;color:#111}
.quote .field{position:absolute;left:80px;width:175px;background:var(--field);border:1px solid #9a9694}
.submit{position:absolute;left:80px;top:264px;width:111px;height:32px;border-radius:16px;background:linear-gradient(#e6a337,#b66a0a);border:1px solid #9a5b08;color:#fff;font-family:"Fjalla One",sans-serif;font-size:15px;display:flex;align-items:center;justify-content:center}

.footer-nav{position:absolute;top:1018px;left:0;width:932px;height:58px;background:linear-gradient(#fafafa,#dedede);border-top:2px solid #c4c4c4;display:flex;justify-content:center;align-items:center;font-size:13px;color:#222;gap:0;padding-left:4px}
.footer-nav .bar{margin:0 15px}

.site-footer{position:absolute;top:1076px;left:0;width:932px;height:124px;background:linear-gradient(#d2d2d2,#9d9d9d);border-top:1px solid #888}
.legal{position:absolute;left:16px;top:42px;font-size:12.5px;line-height:20px;color:#111;font-weight:700}
.legal .first{font-size:14px;font-weight:400}
.social-title{position:absolute;left:631px;top:31px;font-size:12.5px;color:#222}
.social{position:absolute;top:66px;display:flex;align-items:center;gap:14px;font-size:13px;color:#222}
.social-square{width:29px;height:29px;border-radius:3px}
</style>
</head>
<body>

<nav class="utility">
  <a href="#">Login</a><span class="sep">|</span><a href="#">Register</a><span class="sep short">|</span><a href="#">Sitemap</a>
</nav>

<div class="brand">
  <span class="brand-mark"></span>
  <span class="brand-name">Tillbrook</span>
</div>

<nav class="main-nav">
  <ul>
    <li style="left:203px">Home</li>
    <li class="bar" style="left:262px">|</li>
    <li style="left:288px">About Tillbrook</li>
    <li class="bar" style="left:407px">|</li>
    <li class="active" style="left:410px;width:147px">Insurance Lingo</li>
    <li class="bar" style="left:556px">|</li>
    <li style="left:580px">Dealer Locator</li>
    <li class="bar" style="left:697px">|</li>
    <li style="left:722px">Photo Gallery</li>
    <li class="bar" style="left:833px">|</li>
    <li style="left:857px">Contact</li>
  </ul>
</nav>

<section class="showcase">
  <article class="product" style="width:311px">
    <div class="product-photo photo-moto" role="img" aria-label="Red sport motorcycle on a dark studio background"></div>
    <h2 class="product-tab tab-moto"><span class="tab-dot"></span>Motor Cycle Insurance</h2>
    <div class="product-body">
      <p class="lead moto">Duis aute irure dolor in reprehendeit voptate sit nvelit cillum dolore</p>
      <p class="copy">Officia desemrunt mollit anim in laborum excepteur. Sunt in culpa qui officia deserunt mollit anim id est laborum. Duis aue irure dolor sit reprenderit. Excepteur sint occaecat cupidatat proident, sunt deserunt.</p>
      <a class="read-more" href="#">read more</a>
    </div>
  </article>
  <article class="product" style="width:310px">
    <div class="product-photo photo-boat" role="img" aria-label="White motor yacht cruising at speed on open water"></div>
    <h2 class="product-tab tab-boat"><span class="tab-dot"></span>Boat Insurance</h2>
    <div class="product-body">
      <p class="lead boat">Sunt in culpa qui officia deserunt mollit anim id est laborum. Duis aue irure dolor sit ametreprenderit.</p>
      <p class="copy">Desemrunt mollit anim in laborum excepteur. Sunt in culpa qui officia deserunt mollit anim id est laborum. Duis aue irure dolor sit reprenderit.</p>
      <a class="read-more" href="#" style="bottom:17px">read more</a>
    </div>
  </article>
  <article class="product" style="width:311px">
    <div class="product-photo photo-water" role="img" aria-label="Rider on a personal watercraft spraying across turquoise water"></div>
    <h2 class="product-tab tab-water"><span class="tab-dot"></span>Water Crafts Insurance</h2>
    <div class="product-body">
      <p class="lead water">Duis aute irure dolor in reprehendeit voptate sit nvelit cillum dolore</p>
      <p class="copy">Officia desemrunt mollit anim in laborum excepteur. Sunt in culpa qui officia deserunt mollit anim id est laborum. Duis aue irure dolor sit reprenderit. Excepteur sint occaecat cupidatat proident, sunt deserunt.</p>
      <a class="read-more" href="#">read more</a>
    </div>
  </article>
</section>

<section class="services">
  <a class="service" href="#" style="left:34px;top:56px">
    <svg viewBox="0 0 48 48"><circle cx="24" cy="24" r="23" fill="#888"/><circle cx="24" cy="24" r="20" fill="#e2541b"/><circle cx="24" cy="20" r="14" fill="#f5a03a" opacity=".6"/><rect x="15" y="18" width="18" height="12" rx="2" fill="#fff"/><rect x="15" y="21" width="18" height="2.5" fill="#e2541b"/></svg>
    Make Payment
  </a>
  <a class="service" href="#" style="left:313px;top:56px">
    <svg viewBox="0 0 48 48"><circle cx="24" cy="24" r="23" fill="#888"/><circle cx="24" cy="24" r="20" fill="#2fb43a"/><circle cx="24" cy="20" r="14" fill="#8fe36a" opacity=".6"/><path d="M31 15 L19 27 M18 20 V29 H27" stroke="#fff" stroke-width="3.5" fill="none" stroke-linecap="round"/></svg>
    Report A Claim
  </a>
  <div class="divider" style="top:127px"></div>
  <a class="service" href="#" style="left:34px;top:153px">
    <svg viewBox="0 0 48 48"><circle cx="24" cy="24" r="23" fill="#888"/><circle cx="24" cy="24" r="20" fill="#1f8fd0"/><circle cx="24" cy="20" r="14" fill="#7fd6f2" opacity=".6"/><path d="M31 24 A7 7 0 1 1 24 17" stroke="#fff" stroke-width="3" fill="none"/><path d="M22 13 L27 17 L22 21 Z" fill="#fff"/></svg>
    Retrieve a Quote
  </a>
  <a class="service" href="#" style="left:313px;top:153px">
    <svg viewBox="0 0 48 48"><circle cx="24" cy="24" r="23" fill="#888"/><circle cx="24" cy="24" r="20" fill="#a21fc4"/><circle cx="24" cy="20" r="14" fill="#e08af2" opacity=".6"/><circle cx="24" cy="24" r="7" fill="none" stroke="#fff" stroke-width="4" stroke-dasharray="3 2.5"/><circle cx="24" cy="24" r="2.5" fill="#fff"/></svg>
    Print ID Card
  </a>
  <div class="divider" style="top:222px"></div>
  <a class="service" href="#" style="left:34px;top:247px">
    <svg viewBox="0 0 48 48"><circle cx="24" cy="24" r="23" fill="#888"/><circle cx="24" cy="24" r="20" fill="#2a27c8"/><circle cx="24" cy="20" r="14" fill="#8a8af5" opacity=".6"/><path d="M24 14 L27 21 L34 21.5 L28.5 26 L30.5 33 L24 29 L17.5 33 L19.5 26 L14 21.5 L21 21 Z" fill="none" stroke="#fff" stroke-width="2.2" stroke-linejoin="round"/></svg>
    Other Products
  </a>
</section>

<aside class="quote">
  <h2 class="quote-head"><span class="tab-dot"></span>Quick Quote</h2>
  <label style="top:79px">Name</label><div class="field" style="top:62px;height:32px"></div>
  <label style="top:133px">E-Mail</label><div class="field" style="top:118px;height:32px"></div>
  <label style="top:177px">Message</label><div class="field" style="top:177px;height:69px"></div>
  <a class="submit" href="#">Submit</a>
</aside>

<nav class="footer-nav">
  <a href="#">Home</a><span class="bar">|</span>
  <a href="#">About Tillbrook</a><span class="bar">|</span>
  <a href="#">Insurance Lingo</a><span class="bar">|</span>
  <a href="#">Dealer Locator</a><span class="bar">|</span>
  <a href="#">Photo Gallery</a><span class="bar">|</span>
  <a href="#">Contact</a>
</nav>

<footer class="site-footer">
  <p class="legal"><span class="first">© 2011 Tillbrook Insurance Services,</span><br>P.O Box 58, Larkmoor, CA 90512.<br>CA License 0847216 / National Producer No. 612804</p>
  <p class="social-title">Social Networks</p>
  <a class="social" href="#" style="left:632px"><span class="social-square" style="background:#3b5a9a"></span>Linkspace</a>
  <a class="social" href="#" style="left:752px"><span class="social-square" style="background:#5cb8dd"></span>Chatterly</a>
</footer>

</body>
</html>
```